card design for engineering consultancy

engineering drafting and project management company the provides drafting services for.
Electrical, Hydraulic, Mechanical, and Civil services
The company is called Q7R Services and logo is as attached
Information on card should be.
1. Logo
2.website : Q7RServices.example
3. email : info@Q7RServices.example
4. Phone: (+61) 400512836
5. Motto: Design - Document - Develop - Deliver

this card should be basically used for business identification only

Target Market(s)

electricians plumbers air conditioning installers and civil contractors

Industry/Entity Type

engineering, drafting, electrical, plumbing, airconditioning, civil

Contact Information for Business Card

1. Logo 2.website : Q7RServices.example 3. email : info@Q7RServices.example 4. Phone: (+61) 400512836 5. Motto: Design - Document - Develop - Deliver

Font styles to use
Serif

Requirements
Must have
• logo
Nice to have
• something inovative and different that makes it stand out from being just another business card

```html
<!DOCTYPE html>
<html lang="en">
<head>
<meta charset="utf-8">
<title>Q7R Services – Business Card</title>
<link rel="stylesheet" href="https://fonts.googleapis.com/css2?family=Saira:wght@500;600;700&family=Roboto:wght@400&family=Roboto+Condensed:wght@700&display=swap">
<style>
  :root {
    --page-bg: #dcdcdc;
    --card-white: #ffffff;
    --card-dark: #383838;
    --pattern-top: #4c4c4c;
    --ink-dark: #47474a;
    --ink-body: #3d3d3d;
    --brand-red: #d3202e;
    --rule: #dedede;
    --white: #ffffff;
  }
  * { margin: 0; padding: 0; box-sizing: border-box; }
  html, body { width: 1200px; height: 1200px; overflow: hidden; background: var(--page-bg); }
  .stage { position: relative; width: 1200px; height: 1200px; }

  .card {
    position: absolute; top: 293px; width: 351px; height: 614px;
    border-radius: 19px; overflow: hidden;
    box-shadow: 0 18px 40px rgba(0,0,0,.25);
  }
  .card-front { left: 222px; background: var(--card-white); }
  .card-back { left: 627px; background: var(--card-dark); }

  .wordmark {
    position: absolute; left: 0; right: 0; text-align: center;
    font-family: "Saira", sans-serif; font-weight: 700;
    font-size: 34px; letter-spacing: 1px; line-height: 1;
  }
  .card-front .wordmark { top: 132px; color: var(--ink-dark); }
  .card-back .wordmark { top: 430px; color: var(--white); }

  .holder { position: absolute; top: 282px; left: 0; right: 0; text-align: center; }
  .holder-name {
    font-family: "Saira", sans-serif; font-weight: 600;
    font-size: 27px; color: var(--brand-red); line-height: 1.1;
  }
  .holder-role {
    font-family: "Roboto", sans-serif; font-size: 17px;
    color: var(--ink-body); letter-spacing: .5px; margin-top: 1px;
  }

  .contact-list { position: absolute; top: 338px; left: 0; right: 0; list-style: none; }
  .rule { width: 160px; height: 1px; margin: 0 auto; background: var(--rule); }
  .contact-item { text-align: center; padding: 14px 0 7px; }
  .contact-icon {
    display: block; width: 25px; height: 25px; margin: 0 auto 5px;
    border-radius: 4px; background: var(--brand-red);
  }
  .contact-text {
    font-family: "Roboto", sans-serif; font-size: 17px;
    color: var(--ink-body); letter-spacing: .6px; line-height: 20px;
  }
  .contact-item + .rule { margin-bottom: 0; }

  .pattern-field {
    position: absolute; top: 0; left: 0; right: 0; height: 400px;
    background: linear-gradient(180deg, var(--pattern-top) 0%, #444 45%, var(--card-dark) 100%);
  }

  .motto {
    position: absolute; top: 563px; left: 0; right: 0; text-align: center;
    font-family: "Roboto Condensed", sans-serif; font-weight: 700;
    font-size: 17px; color: var(--white); white-space: nowrap;
  }
  .motto .sep { color: var(--brand-red); margin: 0 3px; }
</style>
</head>
<body>
<main class="stage">

  <section class="card card-front" aria-label="Card front">
    <div class="wordmark">Q7R Services</div>

    <div class="holder">
      <div class="holder-name">Daniel Harper</div>
      <div class="holder-role">Technician</div>
    </div>

    <ul class="contact-list">
      <li class="rule" aria-hidden="true"></li>
      <li class="contact-item">
        <svg class="contact-icon" viewBox="0 0 25 25" aria-hidden="true">
          <rect width="25" height="25" rx="4" fill="#d3202e"/>
          <path d="M8.6 6.5c.4-.3 1-.3 1.3.1l1.4 1.9c.3.4.2.9-.1 1.2l-.9.8c.6 1.4 1.7 2.6 3.1 3.2l.8-.9c.3-.3.8-.4 1.2-.1l1.9 1.4c.4.3.4.9.1 1.3l-.9 1c-.6.6-1.5.8-2.3.5-3-1.1-5.3-3.4-6.4-6.4-.3-.8-.1-1.7.5-2.3z" fill="#fff"/>
        </svg>
        <span class="contact-text">(+61) 400512836</span>
      </li>
      <li class="rule" aria-hidden="true"></li>
      <li class="contact-item">
        <svg class="contact-icon" viewBox="0 0 25 25" aria-hidden="true">
          <rect width="25" height="25" rx="4" fill="#d3202e"/>
          <rect x="6.5" y="8" width="12" height="9" rx="1" fill="#fff"/>
          <path d="M6.8 8.6l5.7 4.3 5.7-4.3" fill="none" stroke="#d3202e" stroke-width="1.1"/>
        </svg>
        <span class="contact-text">info@Q7RServices.example</span>
      </li>
      <li class="rule" aria-hidden="true"></li>
      <li class="contact-item">
        <svg class="contact-icon" viewBox="0 0 25 25" aria-hidden="true">
          <rect width="25" height="25" rx="4" fill="#d3202e"/>
          <g fill="none" stroke="#fff" stroke-width="1">
            <circle cx="12.5" cy="12.5" r="6"/>
            <ellipse cx="12.5" cy="12.5" rx="2.6" ry="6"/>
            <path d="M6.5 12.5h12M7.3 9.5h10.4M7.3 15.5h10.4"/>
          </g>
        </svg>
        <span class="contact-text">Q7RServices.example</span>
      </li>
      <li class="rule" aria-hidden="true"></li>
    </ul>
  </section>

  <section class="card card-back" aria-label="Card back">
    <div class="pattern-field" role="img" aria-label="Repeating diagonal brand-mark pattern fading downward"></div>
    <div class="wordmark">Q7R Services</div>
    <p class="motto">Design<span class="sep">-</span> Document <span class="sep">-</span> Develop <span class="sep">-</span> Deliver</p>
  </section>

</main>
</body>
</html>
```